写真挿入は無し、メニュー、営業時間も別看板がありますので記載不要です。添付のロゴとイラストを挿入してください。看板は両面ですが1デザインでも構いません。
⚪店名 雪見坂ことり亭
⚪定食 お酒 または、お食事 呑み処 など(デザインとのバランスでお願いします。)
⚪お気軽にどうぞ、気軽に来店ください など(安心して気軽に入店しやすくなる1フレーズ)
⚪イラストにふき出しで発声させてください。(フレーズはお任せします。)
⚪サイズは450mm×1300mmで縦長です。納品はaiデータです。
⚪文字色、全体的なデザインはお任せですが、背景色は薄ピンクが希望色です。グラデーションも好きです。イラスト、ロゴとのバランスでお願いします。
私ai使えませんので確認は別形式でお願いします。

見やすくバランスが良く丁度良いです。

また、よろしくお願いいたします。

```html
<!DOCTYPE html>
<html lang="ja">
<head>
<meta charset="utf-8">
<title>雪見坂ことり亭 のぼり看板</title>
<link rel="stylesheet" href="https://fonts.googleapis.com/css2?family=Shippori+Mincho+B1:wght@700;800&display=swap">
<style>
  :root {
    --page: #ffffff;
    --pink-deep: #ef7fae;
    --pink-mid: #f6b3cd;
    --pink-soft: #fbe1eb;
    --pink-pale: #fff3f7;
    --ink: #4a2a22;
    --name: #8c2633;
    --stamp: #c8333a;
    --bubble-text: #c8213a;
    --bubble-fill: #ffffff;
    --figure-pink: #f4a6c4;
    --figure-green: #8fc98a;
  }
  html, body {
    margin: 0;
    width: 820px;
    height: 1200px;
    overflow: hidden;
    background: var(--page);
  }
  .canvas {
    position: relative;
    width: 820px;
    height: 1200px;
  }
  .banner {
    position: absolute;
    left: 207px;
    top: 15px;
    width: 406px;
    height: 1170px;
    overflow: hidden;
    background:
      radial-gradient(ellipse 70% 40% at 20% 55%, rgba(255,255,255,0.85), rgba(255,255,255,0) 70%),
      radial-gradient(ellipse 80% 30% at 85% 2%, var(--pink-deep), rgba(239,127,174,0) 80%),
      linear-gradient(180deg, var(--pink-mid) 0%, var(--pink-soft) 45%, var(--pink-soft) 70%, var(--pink-pale) 100%);
  }
  .category {
    position: absolute;
    left: 170px;
    top: 98px;
    margin: 0;
    font-family: "Shippori Mincho B1", serif;
    font-weight: 800;
    font-size: 27px;
    letter-spacing: 1px;
    color: var(--ink);
  }
  .shop-name {
    position: absolute;
    inset: 0;
    margin: 0;
    font-family: "Shippori Mincho B1", serif;
    font-weight: 800;
    color: var(--name);
  }
  .shop-name .line-top {
    position: absolute;
    left: 70px;
    top: 150px;
    font-size: 96px;
    line-height: 1;
    letter-spacing: 2px;
  }
  .shop-name .line-bottom {
    position: absolute;
    left: 160px;
    top: 272px;
    writing-mode: vertical-rl;
    font-size: 68px;
    line-height: 1;
    letter-spacing: 2px;
  }
  .name-stamp {
    position: absolute;
    left: 92px;
    top: 500px;
    width: 22px;
    height: 30px;
    background: var(--stamp);
  }
  .speech-bubble {
    position: absolute;
    left: 190px;
    top: 600px;
    width: 185px;
    height: 100px;
  }
  .speech-bubble p {
    position: absolute;
    inset: 16px 0 0 0;
    margin: 0;
    text-align: center;
    font-family: "Shippori Mincho B1", serif;
    font-weight: 800;
    font-size: 20px;
    line-height: 1.4;
    color: var(--bubble-text);
  }
  .mascot {
    position: absolute;
    left: 222px;
    top: 700px;
    width: 170px;
    height: 450px;
    border-radius: 80px 80px 30px 30px;
    background: linear-gradient(180deg, var(--figure-pink) 0%, var(--figure-pink) 55%, var(--figure-green) 100%);
    opacity: 0.85;
  }
</style>
</head>
<body>
  <div class="canvas">
    <section class="banner">
      <p class="category">お食事・呑み処</p>
      <h1 class="shop-name">
        <span class="line-top">雪見坂</span>
        <span class="line-bottom">ことり亭</span>
      </h1>
      <span class="name-stamp"></span>
      <div class="speech-bubble">
        <svg width="185" height="100" viewBox="0 0 185 100" aria-hidden="true">
          <path d="M20 6 H165 Q180 6 180 20 V70 Q180 84 165 84 H110 L95 98 L88 84 H20 Q6 84 6 70 V20 Q6 6 20 6 Z" fill="var(--bubble-fill)" stroke="#f2b6c9" stroke-width="2"/>
        </svg>
        <p>皆様のお越しを<br>お待ちしてます</p>
      </div>
      <div class="mascot" role="img" aria-label="着物と袴姿の店のマスコットキャラクターのイラスト"></div>
    </section>
  </div>
</body>
</html>
```